Need a sleek, professional business card design for a Web Development business

I need a unique business card designed for a web development company. It is also the parent company for any ventures I do, such as my ClipWave channel, startup ideas I have, etc. I am the single member of "Bright Harbor Code LLC." I will attach my basic logo here, so you will see the current color scheme and have the asset available. Thank you!

Target Market(s)

Startups, SMB's, Professionals

Industry/Entity Type

Business

Font styles to use
Other font styles liked:
• Lovello for headings is what I use, but not necessary.

Colors

Designer to choose colors to be used in the design.

Requirements
Nice to have
• Sleek is the word. Professional, modern, dark.
Should not have
• Any work from someone else's design. Lacking originality.

```html
<!DOCTYPE html>
<html lang="en">
<head>
<meta charset="utf-8">
<title>Bright Harbor Code LLC — Business Card</title>
<link href="https://fonts.googleapis.com/css2?family=Michroma&display=swap" rel="stylesheet">
<style>
  :root {
    --page-bg: #f2f2f2;
    --card-bg: #1e1b19;
    --accent: #f6a65c;
    --accent-deep: #ef6f62;
    --rule: #c9834a;
  }
  * { box-sizing: border-box; margin: 0; padding: 0; }
  html, body {
    width: 1200px;
    height: 1200px;
    overflow: hidden;
    background: var(--page-bg);
  }
  body {
    display: flex;
    align-items: center;
    justify-content: center;
    font-family: "Michroma", sans-serif;
    color: var(--accent);
  }
  .business-card {
    position: relative;
    width: 980px;
    height: 530px;
    background: var(--card-bg);
  }
  .brand-block {
    position: absolute;
    left: 70px;
    top: 120px;
    width: 330px;
    display: flex;
    flex-direction: column;
    align-items: center;
  }
  .brand-square {
    width: 150px;
    height: 150px;
    background: var(--accent-deep);
    border-radius: 8px;
    margin-bottom: 48px;
  }
  .brand-name {
    font-size: 19px;
    letter-spacing: 0.5px;
    white-space: nowrap;
    text-transform: uppercase;
  }
  .brand-suffix {
    display: flex;
    align-items: center;
    gap: 14px;
    margin-top: 8px;
    font-size: 15px;
    letter-spacing: 6px;
  }
  .brand-suffix .rule {
    width: 110px;
    height: 1px;
    background: var(--rule);
  }
  .contact-block {
    position: absolute;
    left: 545px;
    top: 108px;
  }
  .person-name {
    font-size: 30px;
    letter-spacing: 7px;
    white-space: nowrap;
  }
  .person-title {
    font-size: 17px;
    letter-spacing: 6px;
    margin-top: 12px;
    margin-left: 3px;
  }
  .contact-list {
    list-style: none;
    margin-top: 50px;
  }
  .contact-item {
    display: flex;
    align-items: center;
    gap: 20px;
  }
  .contact-item svg { flex: none; fill: var(--accent); }
  .contact-phone {
    font-size: 23px;
    letter-spacing: 6px;
  }
  .contact-email, .contact-web {
    font-size: 13px;
    letter-spacing: 2px;
    margin-top: 22px;
    margin-left: 2px;
  }
  .channel-row {
    display: flex;
    gap: 16px;
    margin-top: 28px;
    font-size: 10.5px;
    letter-spacing: 1px;
    white-space: nowrap;
  }
</style>
</head>
<body>
  <section class="business-card">
    <div class="brand-block">
      <div class="brand-square"></div>
      <div class="brand-name">Bright Harbor Code</div>
      <div class="brand-suffix"><span class="rule"></span>LLC<span class="rule"></span></div>
    </div>

    <div class="contact-block">
      <h1 class="person-name">MILES CARTER</h1>
      <p class="person-title">GENERAL DIRECTOR</p>

      <ul class="contact-list">
        <li class="contact-item contact-phone">
          <svg width="26" height="24" viewBox="0 0 26 24" aria-hidden="true">
            <path d="M2 8c0-4 5-6 11-6s11 2 11 6v2h-6V7.5c-1.5-.6-3.2-.9-5-.9s-3.5.3-5 .9V10H2z"/>
            <path d="M6 12h14l3 10H3z"/>
          </svg>
          <span>555.014.2290</span>
        </li>
        <li class="contact-item contact-email">
          <svg width="26" height="18" viewBox="0 0 26 18" aria-hidden="true">
            <path d="M0 0h26v18H0z"/>
            <path d="M1 1l12 9 12-9" fill="none" stroke="#1e1b19" stroke-width="2"/>
          </svg>
          <span>miles.carter@bhc.com</span>
        </li>
        <li class="contact-item contact-web">
          <svg width="26" height="26" viewBox="0 0 26 26" aria-hidden="true">
            <circle cx="13" cy="13" r="12"/>
            <g fill="none" stroke="#1e1b19" stroke-width="1.6">
              <ellipse cx="13" cy="13" rx="5" ry="12"/>
              <path d="M1 13h24M3 7h20M3 19h20M13 1v24"/>
            </g>
          </svg>
          <span>www.brightharborcode.com</span>
        </li>
      </ul>

      <div class="channel-row">
        <span>ClipWave</span>
        <span>Glint</span>
        <span>Callo</span>
        <span>Pals</span>
        <span>WorkNet</span>
        <span>Tumbo</span>
      </div>
    </div>
  </section>
</body>
</html>
```